Design some Business Card for shipping company

We need a creative business card designed for a shipping company. All relevant information such as address and phone number can be found on our website. Will need a design for both front and back. The front will container our logo, slogan, contact information etc. The back will have a coupon and some text. check out www.talvorfreight.example for all the information. We need something memorable and unique that will stand out. It needs to a horizontal design. Not vertical.

```html
<!DOCTYPE html>
<html lang="en">
<head>
<meta charset="utf-8">
<title>Talvor Freight – Business Cards</title>
<link href="https://fonts.googleapis.com/css2?family=Fira+Sans:wght@600;700&family=Questrial&family=Quicksand:wght@500&display=swap" rel="stylesheet">
<style>
  :root{
    --backdrop:#2b2b2d;
    --card:#ffffff;
    --green:#1f7a45;
    --green-band:#2f8a55;
    --red:#c8202b;
    --red-band:#c73a44;
    --ink:#1b1b1b;
    --black:#111111;
  }
  *{margin:0;padding:0;box-sizing:border-box}
  html,body{width:1200px;height:780px;overflow:hidden;background:var(--backdrop)}
  .canvas{position:relative;width:1200px;height:780px}
  .card{position:absolute;width:600px;height:343px;background:var(--card);overflow:hidden;box-shadow:0 8px 24px rgba(0,0,0,.45)}
  .card--front{left:60px;top:46px}
  .card--back{left:540px;top:410px}
  .card__bands{position:absolute;left:0;bottom:0;width:600px;height:60px}
  .brand{position:absolute;display:flex;align-items:center}
  .brand__dot{border-radius:50%;background:var(--green);flex:none}
  .brand__name{font-family:"Fira Sans",sans-serif;font-weight:700;color:var(--green);text-transform:uppercase;letter-spacing:.5px;line-height:1}
  .brand__slogan{font-family:"Fira Sans",sans-serif;font-weight:700;color:var(--ink);line-height:1.1}
  .card--front .brand{left:42px;top:108px;gap:18px}
  .card--front .brand__dot{width:78px;height:78px}
  .card--front .brand__name{font-size:40px}
  .card--front .brand__slogan{font-size:19px;margin-top:6px}
  .website{position:absolute;left:196px;bottom:22px;font-family:"Quicksand",sans-serif;font-weight:500;font-size:13px;color:#fff;transform:rotate(-3deg)}
  .card--back .brand{left:38px;top:118px;gap:10px}
  .card--back .brand__dot{width:40px;height:40px}
  .card--back .brand__name{font-size:20px}
  .card--back .brand__slogan{font-size:10px;margin-top:3px}
  .notes{position:absolute;left:42px;top:170px;width:240px}
  .notes span{display:block;height:2px;background:var(--red);margin-bottom:21px}
  .person{position:absolute;right:70px;top:26px;text-align:right}
  .person__name{font-family:"Questrial",sans-serif;font-size:34px;color:var(--ink);line-height:1}
  .person__role{font-family:"Questrial",sans-serif;font-size:15px;color:var(--ink)}
  .contact{position:absolute;right:22px;top:120px;list-style:none;font-family:"Quicksand",sans-serif;font-weight:500;font-size:11.5px;color:var(--ink);text-align:right}
  .contact li{display:flex;justify-content:flex-end;align-items:center;gap:10px;height:23px}
  .contact svg{width:16px;height:16px;flex:none}
  .contact .address{align-items:flex-start;height:auto;line-height:1.5}
</style>
</head>
<body>
<main class="canvas">

  <section class="card card--front">
    <div class="brand">
      <span class="brand__dot"></span>
      <div>
        <div class="brand__name">Talvor Freight</div>
        <div class="brand__slogan">Secure Affordable Shipping to Kenya</div>
      </div>
    </div>
    <svg class="card__bands" viewBox="0 0 600 60" aria-hidden="true">
      <polygon points="0,34 185,34 160,60 0,60" fill="var(--black)"/>
      <polygon points="185,34 440,4 405,60 160,60" fill="var(--red-band)"/>
      <polygon points="440,4 600,0 600,60 405,60" fill="var(--green-band)"/>
    </svg>
    <div class="website">www.talvorfreight.example</div>
  </section>

  <section class="card card--back">
    <div class="person">
      <div class="person__name">Mara Velk</div>
      <div class="person__role">Director</div>
    </div>
    <div class="brand">
      <span class="brand__dot"></span>
      <div>
        <div class="brand__name">Talvor Freight</div>
        <div class="brand__slogan">Secure Affordable Shipping to Kenya</div>
      </div>
    </div>
    <div class="notes"><span></span><span></span><span></span><span></span></div>
    <ul class="contact">
      <li>USA: +1 555 014 2290
        <svg viewBox="0 0 16 16"><rect x="4" y="1" width="8" height="14" rx="1.5" fill="var(--red)"/><rect x="5.5" y="3" width="5" height="8" fill="#fff"/></svg></li>
      <li>KENYA: +254700000123, 0700000123
        <svg viewBox="0 0 16 16"><rect x="4" y="1" width="8" height="14" rx="1.5" fill="var(--red)"/><rect x="5.5" y="3" width="5" height="8" fill="#fff"/></svg></li>
      <li>info@talvorfreight.example
        <svg viewBox="0 0 16 16"><rect x="1" y="3" width="14" height="10" rx="1" fill="var(--red)"/><polyline points="1.5,3.5 8,9 14.5,3.5" fill="none" stroke="#fff" stroke-width="1.3"/></svg></li>
      <li>www.talvorfreight.example
        <svg viewBox="0 0 16 16"><circle cx="8" cy="8" r="6.5" fill="none" stroke="var(--red)" stroke-width="1.5"/><ellipse cx="8" cy="8" rx="3" ry="6.5" fill="none" stroke="var(--red)" stroke-width="1.2"/><line x1="1.5" y1="8" x2="14.5" y2="8" stroke="var(--red)" stroke-width="1.2"/></svg></li>
      <li class="address"><span>418 Harbor Loop NE Ste #12<br>Cedarport WA 98000</span>
        <svg viewBox="0 0 16 16"><polygon points="8,1.5 15,8 13,8 13,14 3,14 3,8 1,8" fill="var(--red)"/><rect x="6.5" y="9.5" width="3" height="4.5" fill="#fff"/></svg></li>
    </ul>
    <svg class="card__bands" viewBox="0 0 600 60" aria-hidden="true">
      <polygon points="0,34 150,34 130,60 0,60" fill="var(--black)"/>
      <polygon points="150,34 420,8 390,60 130,60" fill="var(--red-band)"/>
      <polygon points="420,8 600,4 600,60 390,60" fill="var(--green-band)"/>
    </svg>
  </section>

</main>
</body>
</html>
```